Experienced Home remodel service

I'm a home remodeler. I want a catch phrase that clearly describes viewers what kind of work I'm in like the purple phrase on my rough draft idea. I need my website, phone, logo, slogan included. The picture is of my daughter. I want her on it. Be cool if something could be added to her picture like a hard hat or tool belt ect and her picture cut out/background removed. Some kind of background other than plain white for whole picture. I added extra pics of her so pick one

Target Market(s)

Home owners between 30-60

Industry/Entity Type

Home renovation/remodel

Colors

Designer to choose colors to be used in the design.

Requirements
Must have
• Daughters picture incorporated. Logo, phone, website address, slogan,
Nice to have
• See a hardhat or tool belt added to one of my daughters pictures that is chosen to use by designer

```html
<!DOCTYPE html>
<html lang="en">
<head>
<meta charset="utf-8">
<title>Harlow Home Solutions – Billboard</title>
<link href="https://fonts.googleapis.com/css2?family=Anton&family=Poppins:wght@300;500;600;700;800&display=swap" rel="stylesheet">
<style>
  :root {
    --page-bg: #9b9b9b;
    --ink: #111111;
    --band-dark: #0d0d0d;
    --band-mid: #1e1e1e;
    --tile-light: #c9c9c9;
    --tile-mid: #9c9c9c;
    --paper: #f4f4f4;
    --paper-shade: #e2e2e2;
    --white: #ffffff;
    --icon-ring: #d8d8d8;
    --phone-grey: #9a9a9a;
    --photo-lilac: #d9c6e6;
    --photo-yellow: #e9c24a;
  }
  * { box-sizing: border-box; margin: 0; padding: 0; }
  html, body { width: 935px; height: 1200px; overflow: hidden; }
  body { background: var(--page-bg); font-family: "Poppins", sans-serif; position: relative; }

  .billboard {
    position: absolute; left: 30px; top: 383px;
    width: 875px; height: 435px;
    background: linear-gradient(135deg, var(--paper) 0%, var(--white) 45%, var(--paper-shade) 100%);
    box-shadow: 0 6px 14px rgba(0,0,0,.35);
    overflow: hidden;
  }
  .headline-band {
    position: absolute; left: 0; top: 0; width: 100%; height: 293px;
    background:
      linear-gradient(135deg, transparent 0 55%, rgba(255,255,255,.05) 55% 70%, transparent 70%),
      linear-gradient(45deg, transparent 0 60%, rgba(255,255,255,.04) 60% 75%, transparent 75%),
      linear-gradient(180deg, var(--band-mid), var(--band-dark));
  }
  .brand-title {
    position: absolute; left: 32px; top: 26px;
    font-family: "Anton", sans-serif; font-size: 61px; line-height: 1;
    color: var(--white); white-space: nowrap;
  }
  .service { position: absolute; top: 135px; height: 90px; }
  .service--build { left: 32px; width: 203px; background: var(--tile-light); }
  .service--repair { left: 240px; width: 204px; background: var(--tile-mid); }
  .service--replace { left: 448px; width: 192px; background: var(--tile-light); }
  .service__icon {
    position: absolute; left: 50%; top: -28px; transform: translateX(-50%);
    width: 66px; height: 66px; border-radius: 50%;
    background: var(--ink); border: 3px solid var(--icon-ring);
    display: flex; align-items: center; justify-content: center;
  }
  .service__label {
    position: absolute; left: 0; right: 0; bottom: 8px; text-align: center;
    font-weight: 700; font-size: 23px; color: var(--ink); letter-spacing: .3px;
  }
  .tagline {
    position: absolute; left: 29px; top: 243px;
    font-size: 32px; line-height: 1; color: var(--white); white-space: nowrap; letter-spacing: -.3px;
  }
  .tagline__light { font-weight: 300; }
  .tagline__bold { font-weight: 800; letter-spacing: -.9px; }

  .brand-mark {
    position: absolute; left: 35px; top: 305px; width: 120px;
    text-align: center; color: var(--ink);
  }
  .brand-mark__square { width: 34px; height: 34px; background: var(--ink); margin: 4px auto 8px; }
  .brand-mark__name { font-weight: 700; font-size: 10px; line-height: 1.05; letter-spacing: 1px; }
  .brand-mark__line { font-weight: 500; font-size: 6px; letter-spacing: 1.2px; margin-top: 4px; }

  .contact-phone {
    position: absolute; left: 193px; top: 318px;
    display: flex; align-items: center; gap: 13px;
  }
  .contact-phone__icon {
    width: 49px; height: 49px; border-radius: 50%; background: var(--phone-grey);
    display: flex; align-items: center; justify-content: center; flex: none;
  }
  .contact-phone__number { font-weight: 700; font-size: 52px; line-height: 1; color: var(--ink); letter-spacing: -1px; white-space: nowrap; }
  .contact-web {
    position: absolute; left: 193px; top: 372px;
    font-weight: 600; font-size: 26px; color: var(--ink); white-space: nowrap;
  }

  .hero-photo {
    position: absolute; left: 650px; top: 0; width: 205px; height: 435px;
    background: linear-gradient(180deg, #2a2a2a 0%, var(--photo-lilac) 45%, var(--photo-yellow) 78%, #9a9a9a 100%);
  }
</style>
</head>
<body>
  <main class="billboard">
    <section class="headline-band">
      <h1 class="brand-title">HARLOW HOME SOLUTIONS</h1>

      <div class="service service--build">
        <span class="service__icon">
          <svg width="34" height="30" viewBox="0 0 34 30" fill="#fff">
            <rect x="2" y="12" width="13" height="4"/><rect x="17" y="12" width="9" height="4"/>
            <rect x="6" y="18" width="13" height="4"/><rect x="21" y="18" width="11" height="4"/>
            <rect x="2" y="24" width="13" height="4"/><rect x="17" y="24" width="13" height="4"/>
            <path d="M20 10 L30 2 L32 4 L22 12 Z"/>
          </svg>
        </span>
        <span class="service__label">BUILD</span>
      </div>

      <div class="service service--repair">
        <span class="service__icon">
          <svg width="34" height="34" viewBox="0 0 34 34" fill="none" stroke="#fff" stroke-width="4">
            <circle cx="17" cy="17" r="10" stroke-dasharray="5 3"/>
            <path d="M17 10 V27 M13 11 L17 15 L21 11" stroke-linecap="round"/>
          </svg>
        </span>
        <span class="service__label">REPAIR</span>
      </div>

      <div class="service service--replace">
        <span class="service__icon">
          <svg width="34" height="32" viewBox="0 0 34 32" fill="#fff">
            <rect x="17" y="3" width="14" height="10"/><rect x="3" y="19" width="14" height="10"/>
            <path d="M8 15 V8 H13 V5 L16 9 L13 13 V10 H10 V15 Z"/>
            <path d="M26 17 V24 H21 V27 L18 23 L21 19 V22 H24 V17 Z"/>
          </svg>
        </span>
        <span class="service__label">REPLACE</span>
      </div>

      <p class="tagline"><span class="tagline__light">FOR ALL YOUR </span><span class="tagline__bold">HOME REMODEL NEEDS</span></p>
    </section>

    <div class="brand-mark">
      <div class="brand-mark__square"></div>
      <p class="brand-mark__name">HARLOW HOME<br>SOLUTIONS</p>
      <p class="brand-mark__line">BUILD. REPAIR. REPLACE.<br>(555) 014 2730</p>
    </div>

    <div class="contact-phone">
      <span class="contact-phone__icon">
        <svg width="26" height="26" viewBox="0 0 24 24" fill="#fff">
          <path d="M6.6 10.8a15.1 15.1 0 0 0 6.6 6.6l2.2-2.2a1 1 0 0 1 1-.25 11.4 11.4 0 0 0 3.6.57 1 1 0 0 1 1 1V20a1 1 0 0 1-1 1A17 17 0 0 1 3 4a1 1 0 0 1 1-1h3.5a1 1 0 0 1 1 1c0 1.25.2 2.450.57 3.57a1 1 0 0 1-.25 1z"/>
        </svg>
      </span>
      <span class="contact-phone__number">555-014-2730</span>
    </div>
    <p class="contact-web">www.harlowhomesolutions.com</p>

    <div class="hero-photo" role="img" aria-label="Cut-out photo of the owner's young daughter in a yellow hard hat, lilac puffer jacket and tool belt, holding a hammer"></div>
  </main>
</body>
</html>
```